Letterhead and Biz card using my logo
Law Offices of Daniel R. Horvath
Letterhead and Biz card using my logo  - Law
Creative Brief
Professional
The Law Offices of Daniel R. Horvath
41756 County Lane 9 Suite 200 Boca Raton, FL 33517
danielrhorvath@quillpost.net
www.thedebtmender.net
(if you can add this onto the biz card without it looking to busy, use my slogan) "There IS life after bankruptcy."

```html
<!DOCTYPE html>
<html lang="en">
<head>
<meta charset="utf-8">
<title>Law Offices of Daniel R. Horvath – Business Card</title>
<link rel="stylesheet" href="https://fonts.googleapis.com/css2?family=Tinos:wght@400;700&display=swap">
<style>
  :root {
    --bg: #e9eaec;
    --card: #ffffff;
    --card-shade: #eef0f2;
    --blue-deep: #0f4a86;
    --blue-mid: #2a6fb0;
    --blue-light: #4f92cf;
    --rule: #9aa3ad;
    --ink-blue: #1e4f86;
    --ink-dark: #3a3f45;
    --white: #ffffff;
  }
  html, body {
    margin: 0;
    width: 1200px;
    height: 901px;
    overflow: hidden;
    background: var(--bg);
    font-family: "Tinos", "Times New Roman", serif;
  }
  .card {
    position: absolute;
    left: 100px;
    top: 165px;
    width: 1000px;
    height: 571px;
    border-radius: 18px;
    background: linear-gradient(180deg, var(--card) 0%, var(--card-shade) 100%);
    box-shadow: 0 10px 30px rgba(0,0,0,.18);
    overflow: hidden;
  }
  .brand {
    position: absolute;
    left: 170px;
    top: 95px;
    display: flex;
    align-items: center;
    gap: 20px;
  }
  .brand-dot {
    width: 96px;
    height: 96px;
    border-radius: 50%;
    background: var(--blue-mid);
    flex: none;
  }
  .brand-name {
    color: var(--ink-blue);
    font-size: 34px;
    font-weight: 400;
    white-space: nowrap;
  }
  .band {
    position: absolute;
    left: 0;
    right: 0;
    top: 230px;
    height: 166px;
    background: linear-gradient(180deg, var(--blue-light) 0%, var(--blue-mid) 45%, var(--blue-deep) 100%);
    border-top: 4px solid var(--rule);
    border-bottom: 4px solid var(--rule);
  }
  .address {
    position: absolute;
    right: 520px;
    top: 30px;
    color: var(--white);
    font-size: 25px;
    line-height: 34px;
    text-align: right;
    font-style: normal;
    white-space: nowrap;
  }
  .divider {
    position: absolute;
    left: 505px;
    top: 22px;
    width: 2px;
    height: 122px;
    background: rgba(255,255,255,.7);
  }
  .contacts {
    position: absolute;
    left: 530px;
    top: 20px;
    list-style: none;
    margin: 0;
    padding: 0;
    color: var(--white);
    font-size: 24px;
    line-height: 31px;
    white-space: nowrap;
  }
  .contacts li { display: flex; align-items: center; gap: 14px; }
  .contacts svg { width: 20px; height: 20px; flex: none; }
  .website {
    position: absolute;
    left: 210px;
    top: 440px;
    color: var(--ink-dark);
    font-size: 26px;
    letter-spacing: 6px;
    white-space: nowrap;
  }
</style>
</head>
<body>
  <div class="card">
    <div class="brand">
      <div class="brand-dot"></div>
      <div class="brand-name">Law Offices of Daniel R. Horvath</div>
    </div>

    <div class="band">
      <address class="address">
        41756 County Lane 9<br>
        Suite 200<br>
        Boca Raton, FL 33517
      </address>
      <div class="divider"></div>
      <ul class="contacts">
        <li>
          <svg viewBox="0 0 20 20" aria-hidden="true"><path d="M5 2h4l1 5-2.5 1.5a10 10 0 0 0 4 4L13 10l5 1v4c0 1-1 2-2 2C8 17 3 12 3 4c0-1 1-2 2-2z" fill="#fff"/></svg>
          561.555.0142
        </li>
        <li>
          <svg viewBox="0 0 20 20" aria-hidden="true"><rect x="6" y="1" width="8" height="18" rx="2" fill="#fff"/><rect x="7.5" y="3.5" width="5" height="10" fill="#2a6fb0"/></svg>
          561.555.0187
        </li>
        <li>
          <svg viewBox="0 0 20 20" aria-hidden="true"><rect x="5" y="2" width="10" height="5" fill="#fff"/><rect x="2" y="7" width="16" height="8" rx="1" fill="#fff"/><rect x="5" y="13" width="10" height="5" fill="#fff" stroke="#2a6fb0"/></svg>
          561.555.0139
        </li>
        <li>
          <svg viewBox="0 0 20 20" aria-hidden="true"><rect x="2" y="4" width="16" height="12" rx="1" fill="#fff"/><path d="M2.5 4.5 10 11l7.5-6.5" fill="none" stroke="#2a6fb0" stroke-width="1.5"/></svg>
          danielrhorvath@quillpost.net
        </li>
      </ul>
    </div>

    <div class="website">www.thedebtmender.net</div>
  </div>
</body>
</html>
```